Northgate Print and Paper Business

Hi, I need template designs for stationary as listed below using my Logo as per attached file;
1) Business Card (double sided)
2) Letterhead
3) With Compliments Slip
4) Return Address Label (Stickers)

```html
<!DOCTYPE html>
<html lang="en">
<head>
<meta charset="utf-8">
<title>Return Address Label – Northgate Print and Paper Business</title>
<link rel="stylesheet" href="https://fonts.googleapis.com/css2?family=Roboto+Condensed:wght@700&family=Inter:wght@300&display=swap">
<style>
  :root {
    --ink: #231f20;
    --paper: #ffffff;
  }
  html, body {
    margin: 0;
    padding: 0;
    overflow: hidden;
    background: var(--paper);
  }
  .label {
    position: relative;
    width: 1200px;
    height: 472px;
    background: var(--paper);
    color: var(--ink);
    overflow: hidden;
  }
  .label__heading {
    position: absolute;
    left: 32px;
    top: 12px;
    width: 1123px;
    margin: 0;
    font-family: "Roboto Condensed", "Arial Narrow", sans-serif;
    font-weight: 700;
    font-size: 56px;
    line-height: 72px;
    letter-spacing: 2.6px;
    white-space: nowrap;
    border-bottom: 4px solid var(--ink);
  }
  .label__address {
    position: absolute;
    left: 160px;
    top: 0;
    margin: 0;
    font-style: normal;
    font-family: "Inter", "Helvetica Neue", Helvetica, sans-serif;
    font-weight: 300;
    font-size: 60px;
    letter-spacing: -0.5px;
    white-space: nowrap;
  }
  .label__line {
    position: absolute;
    left: 0;
    line-height: 1;
  }
  .label__name   { top: 180px; }
  .label__street { top: 313px; }
  .label__locale { top: 391px; }
  .label__locale span + span { margin-left: 34px; }
</style>
</head>
<body>
  <main class="label">
    <h1 class="label__heading">When not delivered please return to:</h1>
    <address class="label__address">
      <span class="label__line label__name">Penwood Studio by Clara</span>
      <span class="label__line label__street">111 Name Street</span>
      <span class="label__line label__locale"><span>City</span><span>State</span><span>Postcode</span></span>
    </address>
  </main>
</body>
</html>
```